Landing Page for a new, High Production, farming technology

Brightfield Sprout
We need a single landing page, with an email signup for more information.
We build self-contained, farming boxes out of ISO containers. These containers use hydroponics and LED lighting to provide a year round growing environment for crops. So, you could grow crops anywhere at any time of the year in any environment.
For the purpose of this site, we will be doing split testing between several different themes using different sites and keywords.
This site's focus should be providing our product to people searching for high production farming technology.
We'll be focusing on the following key words: Agriculture, aquaponics, farm, garden, hydroponics, organic food, subsistence farming, urban farming, vertical garden.
Target Market(s)
We are going to be using this page to judge that
Number of Pages Required
1 page
Look and feel
Each slider illustrates characteristics of the customer's brand and the style your logo design should communicate.

```html
<!DOCTYPE html>
<html lang="en">
<head>
<meta charset="utf-8">
<title>Brightfield Sprout — High Production Farming Technology</title>
<link href="https://fonts.googleapis.com/css2?family=Montserrat:wght@400;600;700&family=Open+Sans:wght@400;600&display=swap" rel="stylesheet">
<style>
:root{
  --green:#8fb08c;
  --green-dark:#6f926c;
  --orange:#eaa96a;
  --grey:#ebebeb;
  --ink:#1e1e1e;
  --text:#555;
  --white:#fff;
  --black:#151515;
}
*{box-sizing:border-box;margin:0;padding:0}
html,body{width:1200px;height:2844px;overflow:hidden}
body{position:relative;background:var(--white);font-family:"Open Sans",Arial,sans-serif;color:var(--text)}
.abs{position:absolute}

/* hero */
.hero{left:0;top:0;width:1200px;height:740px;background:linear-gradient(180deg,#cfd6cc 0%,#9cb48f 25%,#4f7a3a 55%,#3a5f2c 80%,#6b6454 100%)}
.header{left:0;top:0;width:1200px;height:157px;background:rgba(143,176,140,.88)}
.topbar{left:100px;top:14px;font-size:12px;color:var(--white);display:flex;gap:36px;align-items:center}
.topbar span{display:flex;align-items:center;gap:8px}
.social{right:100px;top:12px;display:flex;gap:10px}
.social i{display:block;width:20px;height:20px;border-radius:50%;background:var(--white)}
.brand{left:100px;top:74px;display:flex;align-items:center;gap:14px}
.brand i{display:block;width:40px;height:40px;border:3px solid var(--white);border-radius:50%;flex:none}
.brand span{font-family:"Montserrat",Arial,sans-serif;font-weight:600;font-size:16px;line-height:20px;letter-spacing:4px;color:var(--white)}
.nav{left:394px;top:88px;display:flex;gap:34px;font-family:"Montserrat",Arial,sans-serif;font-size:11px;color:var(--white);letter-spacing:.3px;white-space:nowrap}
.search{left:1082px;top:84px}
.hero-edge{left:0;top:640px}

/* intro */
.intro-title{left:280px;top:818px;width:292px;text-align:right;font-family:"Montserrat",Arial,sans-serif;font-weight:700;font-size:36px;line-height:42px;color:var(--ink)}
.intro-title span{color:var(--green)}
.intro-rule{left:586px;top:814px;width:2px;height:98px;background:var(--green)}
.intro-kicker{left:612px;top:786px;font-family:"Montserrat",Arial,sans-serif;font-weight:400;font-size:20px;line-height:24px;color:var(--green-dark)}
.intro-copy{left:612px;top:844px;width:410px;font-size:12px;line-height:21px;color:var(--text)}
.intro-copy p{margin-bottom:18px}

/* newsletter */
.newsletter{left:0;width:1200px;height:80px;display:flex;align-items:center}
.newsletter .label{position:absolute;left:262px;font-family:"Montserrat",Arial,sans-serif;font-size:16px;color:var(--white);letter-spacing:.5px}
.newsletter .env{position:absolute;left:194px}
.newsletter .field{position:absolute;left:656px;width:283px;height:32px;background:var(--white)}
.newsletter .btn{position:absolute;left:939px;width:86px;height:32px;background:var(--black);color:var(--white);font-family:"Montserrat",Arial,sans-serif;font-size:12px;font-weight:600;display:flex;align-items:center;justify-content:center}

.band-grey{left:0;width:1200px;background:var(--grey)}
.section-title{left:0;width:1200px;text-align:center;font-family:"Montserrat",Arial,sans-serif;font-weight:700;font-size:34px;color:var(--ink);letter-spacing:.5px}
.section-title span{color:var(--green)}

/* crop tiles */
.tile{top:1562px;width:400px;height:275px}
.tile-label{background:var(--orange);color:var(--ink);font-family:"Montserrat",Arial,sans-serif;font-weight:700;font-size:27px;line-height:34px;padding:14px 22px}

/* gallery */
.gallery-arrow{top:2101px;width:38px;height:38px;border:2px solid var(--ink);border-radius:50%}

/* footer */
.footer{left:0;top:2266px;width:1200px;height:421px;background:linear-gradient(180deg,#394438 0%,#2b3a2a 55%,#3f5a30 100%)}
.footer-h{font-family:"Montserrat",Arial,sans-serif;font-weight:400;font-size:30px;color:var(--white)}
.input{background:var(--white);height:48px;font-size:12px;color:#888;display:flex;align-items:center;gap:8px;padding:0 14px}
.send{border:2px solid var(--white);color:var(--white);font-family:"Montserrat",Arial,sans-serif;font-size:14px;display:flex;align-items:center;justify-content:center}
.addr-h{font-family:"Montserrat",Arial,sans-serif;font-weight:600;font-size:12px;color:var(--white)}
.addr{font-size:12px;line-height:24px;color:var(--white)}
.addr div{display:flex;gap:10px}
.copyright{left:0;top:2768px;width:1200px;height:76px;background:var(--black)}
.copyright p{position:absolute;left:100px;top:30px;font-size:11px;color:#ddd}
.to-top{left:1070px;top:2792px;width:30px;height:30px;border-radius:50%;background:#555}
</style>
</head>
<body>

<!-- hero -->
<div class="abs hero" role="img" aria-label="Greenhouse rows of lettuce growing in hydroponic channels"></div>
<div class="abs header"></div>
<div class="abs topbar">
  <span><svg width="12" height="12" viewBox="0 0 24 24"><path fill="#fff" d="M6.6 10.8a15 15 0 0 0 6.6 6.6l2.2-2.2c.3-.3.7-.4 1-.2 1.1.4 2.3.6 3.6.6.6 0 1 .4 1 1V20c0 .6-.4 1-1 1A17 17 0 0 1 3 4c0-.6.4-1 1-1h3.5c.6 0 1 .4 1 1 0 1.3.2 2.5.6 3.6.1.3 0 .7-.2 1z"/></svg>123-456-789</span>
  <span><svg width="13" height="10" viewBox="0 0 26 20"><rect width="26" height="20" fill="#fff"/><path d="M1 1l12 10L25 1" stroke="#8fb08c" stroke-width="2" fill="none"/></svg>info@domain.com</span>
</div>
<div class="abs social"><i></i><i></i><i></i></div>
<div class="abs brand"><i></i><span>BRIGHTFIELD<br>SPROUT</span></div>
<nav class="abs nav"><span>HOME</span><span>ABOUT US ▾</span><span>CROP PRODUCTION</span><span>LIVESTOCK</span><span>GALLERY ▾</span><span>CONTACT US ▾</span></nav>
<svg class="abs search" width="18" height="18" viewBox="0 0 20 20"><circle cx="8" cy="8" r="6" stroke="#fff" stroke-width="2" fill="none"/><path d="M12.5 12.5L18 18" stroke="#fff" stroke-width="2"/></svg>
<svg class="abs" style="left:98px;top:398px" width="42" height="42" viewBox="0 0 42 42"><circle cx="21" cy="21" r="19" stroke="#fff" stroke-width="2" fill="none"/><path d="M24 13l-8 8 8 8" stroke="#fff" stroke-width="2.5" fill="none"/></svg>
<svg class="abs" style="left:1060px;top:398px" width="42" height="42" viewBox="0 0 42 42"><circle cx="21" cy="21" r="19" stroke="#fff" stroke-width="2" fill="none"/><path d="M18 13l8 8-8 8" stroke="#fff" stroke-width="2.5" fill="none"/></svg>
<svg class="abs hero-edge" width="1200" height="102" viewBox="0 0 1200 102" preserveAspectRatio="none">
  <polygon points="0,60 520,70 900,30 1200,80 1200,102 0,102" fill="#8fb08c"/>
  <polygon points="0,102 0,100 500,90 870,52 1200,102" fill="#fff"/>
</svg>

<!-- intro -->
<h1 class="abs intro-title">BRIGHTFIELD<br><span>SPROUT</span></h1>
<div class="abs intro-rule"></div>
<h2 class="abs intro-kicker">EXPERTS IN<br>CROP PRODUCTION</h2>
<div class="abs intro-copy">
  <p>Lorem Ipsum is simply dummy text of the printing and typesetting industry. Lorem Ipsum has been the industry's standard dummy text ever since the 1500s, when an unknown printer took a galley of type and scrambled it to make a type specimen book.</p>
  <p>It has survived not only five centuries, but also the leap into electronic typesetting, remaining essentially unchanged.</p>
  <p>It was popularised in the 1960s with the release of Letraset sheets containing Lorem Ipsum passages, and more recently with desktop</p>
</div>
<div class="abs" style="left:184px;top:942px;width:404px;height:313px;background:linear-gradient(135deg,#f0f3ef,#c8d8c2 50%,#7fae5e)" role="img" aria-label="Vertical farming racks inside a container"></div>
<div class="abs" style="left:612px;top:1073px;width:404px;height:182px;background:linear-gradient(135deg,#3f6a2c,#6f9a3e 45%,#c0392b 70%,#5b7f33)" role="img" aria-label="Ripe strawberries on the plant"></div>

<!-- newsletter top -->
<div class="abs newsletter" style="top:1340px;background:var(--green)">
  <svg class="env" width="42" height="42" viewBox="0 0 42 42"><path d="M4 18L21 6l17 12v20H4z" fill="none" stroke="#fff" stroke-width="2"/><path d="M4 18l17 12 17-12" fill="none" stroke="#fff" stroke-width="2"/><rect x="11" y="10" width="20" height="14" fill="none" stroke="#fff" stroke-width="1.5"/></svg>
  <span class="label">SIGN UP FOR NEWSLETTER TO GET UPDATES</span>
  <span class="field"></span><span class="btn">SUBSCRIBE</span>
</div>

<!-- crop production -->
<div class="abs band-grey" style="top:1420px;height:142px"></div>
<h2 class="abs section-title" style="top:1475px">CROP <span>PRODUCTION</span></h2>
<div class="abs tile" style="left:0;background:linear-gradient(135deg,#cfe0c4,#7fb04a 50%,#3f6f2a)" role="img" aria-label="Farming box interior with green crops"></div>
<div class="abs tile" style="left:400px;background:linear-gradient(180deg,#eef0f2,#dcdfe2 55%,#8ea37a)" role="img" aria-label="ISO containers in a row"></div>
<div class="abs tile" style="left:800px;background:linear-gradient(180deg,#e9eef0,#c4d1c1 45%,#7da65a)" role="img" aria-label="Hydroponic growing system in a greenhouse"></div>
<div class="abs tile-label" style="left:0;top:1761px">FARMING BOXES</div>
<div class="abs tile-label" style="left:400px;top:1761px">ISO CONTAINERS</div>
<div class="abs tile-label" style="left:800px;top:1752px;padding:6px 22px 8px">HYDROPONIC<br>GROWING SYSTEM</div>

<!-- gallery -->
<div class="abs band-grey" style="top:1837px;height:144px"></div>
<h2 class="abs section-title" style="top:1886px">FEATURED <span>GALLERY</span></h2>
<div class="abs" style="left:150px;top:2023px;width:286px;height:197px;background:linear-gradient(135deg,#6b9a35,#d9a23a 40%,#c0392b 70%,#4f7f2a)" role="img" aria-label="Assorted fresh vegetables"></div>
<div class="abs" style="left:457px;top:2023px;width:286px;height:197px;background:linear-gradient(135deg,#e7ece6,#a9c59a 50%,#7a5a45)" role="img" aria-label="Rows of seedlings in a greenhouse"></div>
<div class="abs" style="left:764px;top:2023px;width:286px;height:197px;background:linear-gradient(135deg,#f2f4f1,#8fcf4a 55%,#e6ebe4)" role="img" aria-label="Young plants in hydroponic pipes"></div>
<svg class="abs gallery-arrow" style="left:98px" width="38" height="38" viewBox="0 0 38 38"><path d="M21 12l-7 7 7 7" stroke="#1e1e1e" stroke-width="2.5" fill="none"/></svg>
<svg class="abs gallery-arrow" style="left:1064px" width="38" height="38" viewBox="0 0 38 38"><path d="M17 12l7 7-7 7" stroke="#1e1e1e" stroke-width="2.5" fill="none"/></svg>

<!-- footer -->
<div class="abs footer" role="img" aria-label="Dimmed greenhouse with lettuce beds in the background"></div>
<svg class="abs" style="left:0;top:2262px" width="1200" height="70" viewBox="0 0 1200 70" preserveAspectRatio="none">
  <polygon points="0,0 1200,0 1200,4 0,4" fill="#fff"/>
  <polygon points="0,4 330,4 0,65" fill="#8fb08c"/>
  <polygon points="0,4 1200,4 1200,30 900,66 320,10" fill="#fff"/>
  <polygon points="900,66 1200,30 1200,60" fill="#8fb08c"/>
</svg>

<h3 class="abs footer-h" style="left:99px;top:2372px">SEND US A MESSAGE</h3>
<div class="abs input" style="left:99px;top:2433px;width:219px"><svg width="11" height="11" viewBox="0 0 20 20"><circle cx="10" cy="6" r="5" fill="#777"/><path d="M1 20c0-6 18-6 18 0z" fill="#777"/></svg>Full Name</div>
<div class="abs input" style="left:99px;top:2491px;width:219px"><svg width="12" height="9" viewBox="0 0 26 20"><rect width="26" height="20" fill="#777"/><path d="M1 1l12 10L25 1" stroke="#fff" stroke-width="2" fill="none"/></svg>Email</div>
<div class="abs input" style="left:99px;top:2550px;width:219px"><svg width="11" height="11" viewBox="0 0 24 24"><path fill="#777" d="M6.6 10.8a15 15 0 0 0 6.6 6.6l2.2-2.2c.3-.3.7-.4 1-.2 1.1.4 2.3.6 3.6.6.6 0 1 .4 1 1V20c0 .6-.4 1-1 1A17 17 0 0 1 3 4c0-.6.4-1 1-1h3.5c.6 0 1 .4 1 1 0 1.3.2 2.5.6 3.6.1.3 0 .7-.2 1z"/></svg>Phone Number</div>
<div class="abs input" style="left:330px;top:2433px;width:258px;height:106px;align-items:flex-start;padding-top:10px">Message</div>
<div class="abs send" style="left:330px;top:2550px;width:258px;height:48px">SEND NOW</div>

<h3 class="abs footer-h" style="left:700px;top:2372px">CONTACT US</h3>
<div class="abs addr-h" style="left:700px;top:2438px">MAIN ADDRESS</div>
<div class="abs addr-h" style="left:925px;top:2438px">POSTAL ADDRESS</div>
<div class="abs addr" style="left:700px;top:2466px;width:210px">
  <div><svg width="12" height="16" viewBox="0 0 12 16"><path d="M6 0a6 6 0 0 1 6 6c0 4-6 10-6 10S0 10 0 6a6 6 0 0 1 6-6z" fill="#eaa96a"/><circle cx="6" cy="6" r="2" fill="#2c3a2c"/></svg><span>Lorem Ipsum is simply<br>dummy text of the printing.</span></div>
  <div style="margin-top:16px"><svg width="12" height="12" viewBox="0 0 24 24"><path fill="#eaa96a" d="M6.6 10.8a15 15 0 0 0 6.6 6.6l2.2-2.2c.3-.3.7-.4 1-.2 1.1.4 2.3.6 3.6.6.6 0 1 .4 1 1V20c0 .6-.4 1-1 1A17 17 0 0 1 3 4c0-.6.4-1 1-1h3.5c.6 0 1 .4 1 1 0 1.3.2 2.5.6 3.6.1.3 0 .7-.2 1z"/></svg><span>123-456-789</span></div>
  <div style="margin-top:20px"><svg width="12" height="10" viewBox="0 0 26 20"><rect width="26" height="20" fill="#eaa96a"/><path d="M1 1l12 10L25 1" stroke="#2c3a2c" stroke-width="2" fill="none"/></svg><span>info@domain.com</span></div>
</div>
<div class="abs addr" style="left:925px;top:2466px;width:210px">
  <div><svg width="12" height="16" viewBox="0 0 12 16"><path d="M6 0a6 6 0 0 1 6 6c0 4-6 10-6 10S0 10 0 6a6 6 0 0 1 6-6z" fill="#eaa96a"/><circle cx="6" cy="6" r="2" fill="#2c3a2c"/></svg><span>Lorem Ipsum is simply<br>dummy text of the printing.<br>123-456-789<br>info@domain.com</span></div>
</div>

<!-- newsletter bottom -->
<div class="abs newsletter" style="top:2687px;height:81px;background:var(--orange)">
  <svg class="env" width="42" height="42" viewBox="0 0 42 42"><path d="M4 18L21 6l17 12v20H4z" fill="none" stroke="#fff" stroke-width="2"/><path d="M4 18l17 12 17-12" fill="none" stroke="#fff" stroke-width="2"/><rect x="11" y="10" width="20" height="14" fill="none" stroke="#fff" stroke-width="1.5"/></svg>
  <span class="label">SIGN UP FOR NEWSLETTER TO GET UPDATES</span>
  <span class="field"></span><span class="btn">SUBSCRIBE</span>
</div>

<div class="abs copyright"><p>Copyright © 2018 Brightfield Sprout - All rights reserved.</p></div>
<svg class="abs to-top" width="30" height="30" viewBox="0 0 30 30"><path d="M9 18l6-6 6 6" stroke="#151515" stroke-width="2.5" fill="none"/></svg>

</body>
</html>
```